Business card and stationary design
Lindora Development
Business card and stationary design -
Creative Brief
Simple
Marike Holzner - van Brugt
MSc, Dipl. Coach & Consultant
Feldrainweg 14 6318 Cham Switzerland
info@lindoradevelopment.ch
www.lindoradevelopment.ch
We're not sure about the font-type, could be the Logo-type or something that's compatible
Personal Coaching Health Coaching Business Coaching Consultancy out of the box, into the outdoors

```html
<!DOCTYPE html>
<html lang="en">
<head>
<meta charset="utf-8">
<title>Lindora Development – Business Cards</title>
<link rel="stylesheet" href="https://fonts.googleapis.com/css2?family=Arimo:wght@400;700&display=swap">
<style>
  :root {
    --stage: #d9d9d9;
    --card: #ffffff;
    --card-shade: #eef0f1;
    --ink: #3a3a3a;
    --ink-soft: #6b6b6b;
    --brand-blue: #1f5fb4;
    --brand-blue-deep: #0f3f8c;
    --brand-blue-light: #4f93dc;
    --leaf: #7cc242;
    --leaf-deep: #3aa43a;
    --lime: #c9e34a;
    --divider: #b9bcc0;
  }
  * { box-sizing: border-box; margin: 0; padding: 0; }
  html, body { width: 1200px; height: 833px; overflow: hidden; }
  body {
    position: relative;
    background: var(--stage);
    font-family: "Arimo", Arial, sans-serif;
    color: var(--ink);
  }
  .card {
    position: absolute;
    border-radius: 14px;
    overflow: hidden;
    box-shadow: 0 4px 14px rgba(0,0,0,.22);
  }
  .card--front { left: 283px; top: 115px; width: 547px; height: 281px;
    background: linear-gradient(180deg, var(--card) 60%, var(--card-shade)); }
  .card--back-white { left: 120px; top: 427px; width: 499px; height: 295px;
    background: linear-gradient(180deg, var(--card) 55%, var(--card-shade)); }
  .card--back-green { left: 643px; top: 427px; width: 504px; height: 295px;
    background: linear-gradient(90deg, var(--lime) 0%, var(--leaf) 45%, var(--leaf-deep) 100%); }

  .brand {
    position: absolute;
    display: flex; align-items: center; gap: 10px;
    font-weight: 700; color: var(--brand-blue);
    text-transform: uppercase; letter-spacing: 1px;
  }
  .brand__dot { flex: none; border-radius: 50%; background: var(--brand-blue); }
  .card--front .brand { left: 30px; top: 104px; font-size: 17px; width: 170px; line-height: 1.15; }
  .card--front .brand__dot { width: 22px; height: 22px; }

  .vline { position: absolute; width: 1px; background: var(--divider); }
  .card--front .vline { left: 212px; top: 38px; height: 150px; }
  .card--back-white .vline { left: 248px; top: 88px; height: 118px; }

  .contact { position: absolute; left: 228px; top: 40px; font-size: 10px; line-height: 1.45; color: var(--ink-soft); }
  .contact__name { font-size: 14px; font-weight: 700; color: var(--ink); line-height: 1.2; }
  .contact__role { font-size: 10px; margin-bottom: 14px; }
  .contact__address { margin-bottom: 12px; }

  .web-band {
    position: absolute; left: 0; right: 0; top: 220px; height: 28px;
    background: linear-gradient(90deg, var(--brand-blue-light), var(--brand-blue) 40%, var(--brand-blue-deep));
    color: #fff; font-size: 10px; letter-spacing: 1.5px;
    display: flex; align-items: center; justify-content: flex-end; padding-right: 140px;
  }

  .card--back-white .brand { left: 28px; top: 130px; font-size: 18px; width: 200px; line-height: 1.15; }
  .card--back-white .brand__dot { width: 24px; height: 24px; }

  .services { position: absolute; list-style: none; }
  .card--back-white .services { left: 262px; top: 92px; font-size: 16px; font-weight: 700; line-height: 27px; color: var(--ink); }
  .services li { display: flex; align-items: center; gap: 6px; }
  .bullet { width: 12px; height: 12px; border-radius: 50%; flex: none;
    background: radial-gradient(circle at 35% 35%, var(--lime), var(--leaf-deep)); }

  .card--back-green .brand { left: 0; right: 0; top: 100px; justify-content: center;
    color: #fff; font-size: 22px; }
  .card--back-green .brand__dot { width: 28px; height: 28px; background: #fff; }

  .card--back-green .services { left: 0; right: 0; top: 226px; font-size: 14px; font-weight: 700; color: #fff;
    display: flex; flex-wrap: wrap; justify-content: center; gap: 4px 10px; padding: 0 40px; }
  .card--back-green .services li + li::before { content: "|"; margin-right: 8px; font-weight: 400; }
  .card--back-green .services li:nth-child(3)::before { content: none; }
  .card--back-green .bullet { background: radial-gradient(circle at 35% 35%, #e9f7c4, #8fd14f); }
</style>
</head>
<body>

<section class="card card--front" aria-label="Business card front">
  <div class="brand"><span class="brand__dot"></span><span>Lindora Development</span></div>
  <div class="vline"></div>
  <div class="contact">
    <p class="contact__name">Marike Holzner - van Brugt</p>
    <p class="contact__role">MSc, Dipl. Coach &amp; Consultant</p>
    <p class="contact__address">Feldrainweg 14<br>6318 Cham, Switzerland</p>
    <p>P: +41 (0)41 555 01 20</p>
    <p>C: +41 (0)78 555 03 47</p>
    <p>E: info@lindoradevelopment.ch</p>
  </div>
  <div class="web-band">www.lindoradevelopment.ch</div>
</section>

<section class="card card--back-white" aria-label="Business card back, white">
  <div class="brand"><span class="brand__dot"></span><span>Lindora Development</span></div>
  <div class="vline"></div>
  <ul class="services">
    <li><span class="bullet"></span>Personal Coaching</li>
    <li><span class="bullet"></span>Health Coaching</li>
    <li><span class="bullet"></span>Business Coaching</li>
    <li><span class="bullet"></span>Consultancy</li>
  </ul>
</section>

<section class="card card--back-green" aria-label="Business card back, green">
  <div class="brand"><span class="brand__dot"></span><span>Lindora Development</span></div>
  <ul class="services">
    <li><span class="bullet"></span>&nbsp;Personal Coaching</li>
    <li><span class="bullet"></span>&nbsp;Health Coaching</li>
    <li><span class="bullet"></span>&nbsp;Business Coaching</li>
    <li><span class="bullet"></span>&nbsp;Consultancy</li>
  </ul>
</section>

</body>
</html>
```